Industrial Company needing new business cards

We are a newly branded Industrial trade company. We specialise in Electrical, Mechanical and Air-conditioning.

I would like to see designs single sided. Focusing on the color scheme white/red/black and possibly gray. Possibly make it a black card with white writting... but open to all designs.

I would like the design to be professional, sleek and to the point.

Industry/Entity Type

Business

Contact Information for Business Card

Tom Harwick
Managing Director / Electrician
tomwork@velnet.com.au
47 Garnet Road, Rutherford NSW 2320
Mobile: 0427115830
www.harwickindustrialgroup.com.au

Requirements
Must have
• Must be able to be sent in a manner that i can change the details for each employee.
• Our logo
Nice to have
• Would like it to somehow have " incorporating Talvo Group Pty Ltd" as this is the company we have taken over.
Should not have
• No yellow!!!
• must not simply place "talvo group" randomly on the business card. refer nice to have.

```html
<!DOCTYPE html>
<html lang="en">
<head>
<meta charset="utf-8">
<title>Harwick Industrial Group – Business Card</title>
<link rel="stylesheet" href="https://fonts.googleapis.com/css2?family=Jost:wght@400;500;700;800&display=swap">
<style>
  :root {
    --page-bg: #ffffff;
    --card-bg: #ffffff;
    --card-edge: #7a7a7a;
    --ink: #1c1c1c;
    --ink-soft: #2b2b2b;
    --grey: #8a8a8a;
    --grey-light: #b9b9b9;
    --red: #e3262b;
  }
  * { margin: 0; padding: 0; box-sizing: border-box; }
  html, body {
    width: 821px;
    height: 1200px;
    overflow: hidden;
    background: var(--page-bg);
    font-family: "Jost", sans-serif;
    color: var(--ink);
  }
  .business-card {
    position: absolute;
    left: 50px;
    top: 380px;
    width: 721px;
    height: 440px;
    background: var(--card-bg);
    border: 1px solid var(--card-edge);
    overflow: hidden;
  }
  .brand {
    position: absolute;
    left: 36px;
    top: 38px;
    display: flex;
    align-items: center;
    gap: 12px;
  }
  .brand-square {
    width: 14px;
    height: 14px;
    background: var(--red);
  }
  .brand-name {
    font-weight: 800;
    font-size: 30px;
    line-height: 1;
    letter-spacing: 1px;
    color: var(--ink);
    text-transform: uppercase;
  }
  .services {
    position: absolute;
    left: 36px;
    top: 90px;
    font-weight: 500;
    font-size: 13.5px;
    letter-spacing: 0.6px;
    color: var(--grey);
    text-transform: uppercase;
  }
  .contact-list {
    position: absolute;
    left: 36px;
    top: 276px;
    list-style: none;
    font-size: 16px;
    line-height: 27px;
    color: var(--ink-soft);
  }
  .incorporating {
    position: absolute;
    left: 36px;
    top: 370px;
    padding-left: 6px;
    border-left: 2px solid var(--red);
    font-size: 12px;
    line-height: 14px;
    color: var(--grey-light);
  }
  .person {
    position: absolute;
    right: 48px;
    top: 276px;
    text-align: right;
  }
  .person-name {
    font-weight: 700;
    font-size: 30px;
    line-height: 36px;
    color: var(--ink);
  }
  .person-name .first { color: var(--grey); }
  .person-role {
    font-size: 15px;
    line-height: 22px;
    color: var(--ink-soft);
  }
  .name-marker {
    position: absolute;
    right: 0;
    top: 276px;
    width: 28px;
    height: 54px;
    background: var(--red);
  }
</style>
</head>
<body>
  <article class="business-card">
    <div class="brand">
      <span class="brand-square"></span>
      <span class="brand-name">Harwick Industrial Group</span>
    </div>
    <p class="services">Electrical - Mechanical - Airconditioning</p>

    <ul class="contact-list">
      <li>tomwork@velnet.com.au</li>
      <li>Mobile: 0427115830</li>
      <li>www.harwickindustrialgroup.com.au</li>
    </ul>

    <p class="incorporating">Incorporating Talvo Group Pty Ltd</p>

    <div class="person">
      <p class="person-name"><span class="first">Tom</span> Harwick</p>
      <p class="person-role">Managing Director / Electrician</p>
    </div>
    <span class="name-marker"></span>
  </article>
</body>
</html>
```